BRISK Signal Partners Business Card Rebrand

Hello Designers! We are looking for help designing our new business card to go in conjunction with our company rebrand. Unfortunately, we have an event mid June that requires we get these printed ASAP (before our new website is launched.) We have a mostly complete Brand Book which I have uploaded to this request for your reference to company information, style, fonts. I've also enclosed our logo file in .eps & .jpg. Attached is a sample business card my boss liked but said was "too simple." I made it in Canva and do not profess to be a designer. NOT FOR DESIGN REFERENCE, ONLY FOR CONTEXT Here is what our old website looks like: https://brisksignalpartners-demo.net/.
Sick
Sick
Sick

```html
<!DOCTYPE html>
<html lang="en">
<head>
<meta charset="utf-8">
<title>BRISK Signal Partners – Business Card</title>
<link href="https://fonts.googleapis.com/css2?family=Montserrat:wght@400;600;800&display=swap" rel="stylesheet">
<style>
  :root{
    --sky:#4db3e6;
    --ink:#111111;
    --paper:#ffffff;
    --stage:#8c8c8c;
    --muted:#3a3a3a;
  }
  *{box-sizing:border-box;margin:0;padding:0}
  html,body{width:1200px;height:721px;overflow:hidden}
  body{
    background:var(--stage);
    font-family:"Montserrat",Arial,sans-serif;
    position:relative;
  }
  .card{
    position:absolute;
    top:212px;
    width:520px;height:297px;
    border-radius:18px;
    overflow:hidden;
    box-shadow:0 10px 28px rgba(0,0,0,.28);
  }
  .card-back{left:50px;background:var(--sky)}
  .card-front{left:630px;background:var(--paper)}

  .brand{display:flex;align-items:center;position:absolute}
  .brand-dot{border-radius:50%;flex:none}
  .brand-name{font-weight:800;line-height:1.05;letter-spacing:.5px;text-transform:uppercase}

  .card-back .brand{left:50%;top:50%;transform:translate(-50%,-50%);gap:16px}
  .card-back .brand-dot{width:92px;height:92px;background:var(--paper)}
  .card-back .brand-name{color:var(--paper);font-size:30px}

  .card-front .brand{left:70px;top:62px;gap:14px}
  .card-front .brand-dot{width:74px;height:74px;background:var(--sky)}
  .card-front .brand-name{color:var(--ink);font-size:24px}

  .contact{
    position:absolute;left:252px;top:158px;
    border-left:1px solid var(--sky);
    padding-left:14px;
    list-style:none;
    font-size:11.5px;color:var(--ink);
  }
  .contact li{display:flex;align-items:center;gap:6px;margin-bottom:6px}
  .contact svg{width:11px;height:11px;flex:none;fill:var(--sky)}

  .person{position:absolute;left:34px;top:210px}
  .person-name{color:var(--sky);font-size:20px;font-weight:400}
  .person-title{color:var(--ink);font-size:12px;font-weight:600;margin-top:4px}

  .location-tab{
    position:absolute;right:0;bottom:0;
    width:240px;height:52px;
    background:var(--sky);
    border-top-left-radius:28px;
    color:var(--paper);font-size:12px;
    display:flex;align-items:center;justify-content:center;
  }
</style>
</head>
<body>
  <section class="card card-back" aria-label="Card back">
    <div class="brand">
      <span class="brand-dot"></span>
      <span class="brand-name">BRISK Signal<br>Partners</span>
    </div>
  </section>

  <section class="card card-front" aria-label="Card front">
    <div class="brand">
      <span class="brand-dot"></span>
      <span class="brand-name">BRISK Signal<br>Partners</span>
    </div>

    <ul class="contact">
      <li><svg viewBox="0 0 24 24" aria-hidden="true"><path d="M6.6 10.8a15 15 0 0 0 6.6 6.6l2.2-2.2a1 1 0 0 1 1-.25 11.4 11.4 0 0 0 3.6.57 1 1 0 0 1 1 1V20a1 1 0 0 1-1 1A17 17 0 0 1 3 4a1 1 0 0 1 1-1h3.5a1 1 0 0 1 1 1c0 1.25.2 2.45.57 3.6a1 1 0 0 1-.25 1z"/></svg>+945-555-0142</li>
      <li><svg viewBox="0 0 24 24" aria-hidden="true"><path d="M2 5h20v14H2zm2 2v.5l8 5 8-5V7z"/></svg>martin@brisksignalpartners-demo.net</li>
      <li><svg viewBox="0 0 24 24" aria-hidden="true"><path d="M12 2a10 10 0 1 0 0 20 10 10 0 0 0 0-20zm0 2c1.2 0 2.6 2.4 3 6H9c.4-3.6 1.8-6 3-6zM4.1 11h3c.1 1.5.3 2.9.7 4H5a8 8 0 0 1-.9-4zm12.8 0h3a8 8 0 0 1-.9 4h-2.8c.4-1.1.6-2.5.7-4zM9 13h6c-.4 3.6-1.8 7-3 7s-2.6-3.4-3-7z"/></svg>www.brisksignalpartners-demo.net</li>
    </ul>

    <div class="person">
      <p class="person-name">Martin Lowe-Harding</p>
      <p class="person-title">Inhaber</p>
    </div>

    <div class="location-tab">Riverton, GA Based (Central Time)</div>
  </section>
</body>
</html>
```